Book covers (2) for a fun new series, Harrowfield Mercy Quiet Capers

I am starting a new book series and am looking for someone to work with over an extended period of time. I will need both e-book and print covers. (This assignment is for the first two books, with more coming soon!) This is a Cozy Mystery Series (a lighter approach to murder and mayhem) with a companion Romance Series. I want both series to have a similar look but a distinguishable difference-- perhaps the dominate color, etc. For the romance, a blue background is a must. While I want each book to be unique, I want all covers easily recognizable as part of the series, so it needs some element of consistency. I will provide the logo. The setting is Harrowfield Mercy Hospital and all stories will tie into the medical field, primarily nursing. Please submit one cover for Book One from each series."Riverbolt Best-Selling Author Dorrie Plaskett"
"The Fender Bender Files"
"A Patchwork Promise"
I'm still waiting on the correct logo files to share with you, so I'm extending the deadline. Thank you for your patience and understanding.
Book Readers, all ages
Designer to choose colors to be used in the design.
- Must show well in thumbnail view
- Relate to medical field / hospital
- Similar element to tie the series together. My thought was to have the same partial hospital image in the background, with a unique focal image dominating each cover.
- Some element of a blue background for the romance -- perhaps the sky; not the entire book!
- Note: The Fender Bender Files is a hit and run by a '75 blue Corveen Dash car; not necessary to have, but may be useful
- If covers include models, I prefer back or side views/ vague imagines. No faces close-ups.
- Nothing steamy for the romance-- these are 'clean' love stories. Should look sweet, not comical.

```html
<!DOCTYPE html>
<html lang="en">
<head>
<meta charset="utf-8">
<title>The Fender Bender Files – Print Cover</title>
<link rel="stylesheet" href="https://fonts.googleapis.com/css2?family=Archivo+Black&family=EB+Garamond&family=Montserrat:wght@300;800&display=swap">
<style>
  :root {
    --page-bg: #f1f1f1;
    --cover-black: #050506;
    --sky-blue: #1e3d8c;
    --author-blue: #2150b0;
    --text-white: #ffffff;
    --body-text: #e9e9e9;
  }
  * { margin: 0; padding: 0; box-sizing: border-box; }
  html, body { width: 899px; height: 1200px; overflow: hidden; }
  body { background: var(--page-bg); position: relative; }

  .spread {
    position: absolute;
    left: 19px; top: 302px;
    width: 1096px; height: 758px;
    transform: scale(0.785);
    transform-origin: top left;
    background: var(--cover-black);
    overflow: hidden;
  }

  /* Back cover */
  .back-cover { position: absolute; left: 0; top: 0; width: 510px; height: 758px; }
  .blurb {
    position: absolute; left: 36px; top: 34px; width: 438px;
    font-family: "EB Garamond", Georgia, serif;
    font-size: 14.6px; line-height: 18.4px;
    color: var(--body-text); text-align: justify; hyphens: auto;
  }
  .blurb p + p { margin-top: 18px; }
  .series-mark {
    position: absolute; left: 36px; top: 628px;
    display: flex; align-items: center; gap: 8px;
  }
  .series-mark .square { width: 22px; height: 22px; background: var(--text-white); }
  .series-mark .name {
    font-family: "EB Garamond", Georgia, serif;
    font-size: 14px; line-height: 16px; color: var(--text-white); width: 110px;
  }

  /* Spine */
  .spine { position: absolute; left: 518px; top: 0; width: 62px; height: 758px; }
  .spine-title {
    position: absolute; left: 12px; top: 34px;
    writing-mode: vertical-rl;
    font-family: "Archivo Black", "Arial Black", sans-serif;
    font-size: 22px; letter-spacing: -0.5px; color: var(--text-white);
  }
  .spine-author {
    position: absolute; left: 18px; top: 528px;
    writing-mode: vertical-rl;
    font-family: "Montserrat", Arial, sans-serif; font-weight: 300;
    font-size: 16px; letter-spacing: 6px; color: var(--author-blue);
  }

  /* Front cover */
  .front-cover {
    position: absolute; left: 590px; top: 0; width: 506px; height: 758px;
    background: linear-gradient(to bottom, var(--sky-blue) 0%, var(--sky-blue) 55%, #0c1a3c 66%, var(--cover-black) 74%);
  }
  .title {
    position: absolute; left: 22px; top: 28px; width: 470px;
    font-family: "Archivo Black", "Arial Black", sans-serif;
    color: var(--text-white); letter-spacing: -3px; line-height: 0.93;
  }
  .title .line-large { display: block; font-size: 98px; }
  .title .line-small { display: block; font-size: 80px; }
  .hospital-art {
    position: absolute; left: 0; top: 372px; width: 506px; height: 186px;
    background: linear-gradient(to bottom, #2a3c6e 0%, #3b3f55 40%, #16181f 80%, var(--cover-black) 100%);
  }
  .author {
    position: absolute; left: 34px; top: 624px;
    font-family: "Montserrat", Arial, sans-serif; font-weight: 300;
    font-size: 38px; letter-spacing: 8px; color: var(--author-blue); white-space: nowrap;
  }
  .tagline {
    position: absolute; left: 34px; top: 678px;
    font-family: "Montserrat", Arial, sans-serif; font-weight: 800;
    font-size: 21.5px; color: var(--author-blue); white-space: nowrap;
  }
</style>
</head>
<body>
  <div class="spread">
    <section class="back-cover">
      <div class="blurb">
        <p>Lorem ipsum dolor sit amet, consectetur adipiscing elit. Phasellus porta, est vitae porta eleifend, quam justo maximus purus, at sodales magna sapien non sapien. Morbi mattis luctus arcu, sed ullamcorper nisi accumsan nec. Integer non metus sed lorem lacinia molestie. Nulla porttitor mauris euismod sem consequat tincidunt. Duis hendrerit erat a tellus ullamcorper mattis. Maecenas eu risus convallis, porttitor mauris eu, hendrerit nulla. Aliquam mauris magna, aliquet at justo sodales, cursus sagittis mauris. Duis aliquam lorem vitae suscipit viverra. Phasellus sed mauris elit. Quisque eleifend nibh placerat lectus faucibus, sed varius arcu posuere. Cras vulputate urna tempus urna tempus, nec molestie tellus posuere. In posuere ligula in sapien tempus tempor. Vestibulum id metus malesuada, aliquam mi aliquam, commodo risus. Aenean et facilisis tellus. Ut interdum varius libero, ut molestie orci fringilla non. Morbi malesuada blandit accumsan.</p>
        <p>Morbi finibus gravida fermentum. Donec in auctor mauris. Aliquam felis lacus, cursus in ullamcorper vel, semper at diam. Nam facilisis hendrerit diam quis fringilla. Maecenas aliquam, nibh et pretium rhoncus, felis mi ornare purus, at convallis ex orci et arcu. Nullam pulvinar porta magna. Fusce aliquam nunc sapien, eu porta mauris viverra vel. Fusce efficitur suscipit neque sed maximus. Etiam imperdiet libero non nibh blandit faucibus. Quisque imperdiet risus non sagittis egestas. Nunc porttitor quis nulla quis maximus. Aliquam hendrerit, ante sit amet ultrices tincidunt, elit lacus rutrum est, non imperdiet ligula enim vitae magna. Class aptent taciti sociosqu ad litora torquent per conubia nostra, per inceptos himenaeos. Mauris id molestie leo. Aliquam feugiat urna ac ex tempus consectetur.</p>
      </div>
      <div class="series-mark">
        <span class="square"></span>
        <span class="name">Harrowfield Mercy Quiet Capers</span>
      </div>
    </section>

    <section class="spine">
      <span class="spine-title">THE FENDER BENDER FILES</span>
      <span class="spine-author">DORRIE PLASKETT</span>
    </section>

    <section class="front-cover">
      <h1 class="title">
        <span class="line-large">THE</span>
        <span class="line-small">FENDER</span>
        <span class="line-small">BENDER</span>
        <span class="line-large">FILES</span>
      </h1>
      <div class="hospital-art" role="img" aria-label="Harrowfield Mercy Hospital building at dusk"></div>
      <p class="author">DORRIE PLASKETT</p>
      <p class="tagline">RIVERBOLT BEST-SELLING AUTHOR</p>
    </section>
  </div>
</body>
</html>
```